App to track miniature golf scores and provides clues to puzzles (Pemberly Under Glass)

A mini-golf scorecard, selfies, badges, rules and clues. See attached for details. The coding and deployment will be provided by someone else, but those requirements are also listed in doc. We need to be able to update any text fields after design is handed over. This app is only for ios.

Target Market(s)

Families

Industry/Entity Type

Entertainment

Requirements
Must have
• The pages listed in the document is needed. Colors are also provided.
Nice to have
• Small animation effects
Should not have
• dark or psychedelic

```html
<!DOCTYPE html>
<html lang="en">
<head>
<meta charset="utf-8">
<title>Pemberly Under Glass – Badges</title>
<link rel="stylesheet" href="https://fonts.googleapis.com/css2?family=Barlow+Condensed:wght@500;600&family=Barlow:wght@400;500&display=swap">
<style>
  :root {
    --canvas: #f4f4f6;
    --screen: #ffffff;
    --ink: #1c1c22;
    --line: #1c1c22;
    --purple: #d48ef2;
    --green: #8cefc4;
    --pink: #f2a9ca;
    --yellow: #fde3a0;
    --icon-purple: #b44fe0;
    --icon-gold: #e8b720;
    --icon-green: #27b874;
    --icon-pink: #e8589a;
  }
  * { box-sizing: border-box; margin: 0; padding: 0; }
  html, body { width: 1200px; height: 675px; overflow: hidden; }
  body {
    background: var(--canvas);
    display: flex; align-items: center; justify-content: center;
    font-family: "Barlow", "Helvetica Neue", Arial, sans-serif;
    color: var(--ink);
  }
  .app-screen {
    position: relative;
    width: 330px; height: 645px;
    background: var(--screen);
    overflow: hidden;
    box-shadow: 0 6px 24px rgba(0,0,0,.08);
  }
  .screen-shapes { position: absolute; inset: 0; z-index: 0; }
  .status-bar {
    position: relative; z-index: 1;
    height: 30px; padding: 8px 18px 0;
    font: 600 12px "Barlow", sans-serif;
    display: flex; justify-content: space-between;
  }
  .app-header {
    position: relative; z-index: 1;
    height: 36px; display: flex; align-items: center; justify-content: center;
  }
  .back-arrow { position: absolute; left: 14px; top: 8px; }
  .screen-title {
    font: 600 20px "Barlow Condensed", sans-serif;
    letter-spacing: .06em; text-transform: uppercase;
  }
  .badge-list {
    position: relative; z-index: 1;
    list-style: none;
    padding: 10px 22px 0;
    display: flex; flex-direction: column; gap: 9px;
  }
  .badge-card {
    height: 74px;
    background: var(--screen);
    border: 1.5px solid var(--line);
    box-shadow: 3px 3px 0 rgba(28,28,34,.12);
    display: flex; align-items: center; gap: 12px;
    padding: 0 12px;
  }
  .badge-icon { flex: 0 0 32px; height: 32px; }
  .badge-text { font-size: 11.5px; line-height: 1.35; }
  .next-button {
    position: absolute; z-index: 1;
    left: 50%; bottom: 14px; transform: translateX(-50%);
    width: 120px; height: 30px;
    background: var(--screen);
    border: 1.5px solid var(--line);
    font: 600 13px "Barlow Condensed", sans-serif;
    letter-spacing: .08em;
    display: flex; align-items: center; justify-content: center;
  }
</style>
</head>
<body>
  <main class="app-screen" aria-label="Pemberly Under Glass badges screen">
    <svg class="screen-shapes" viewBox="0 0 330 645" aria-hidden="true">
      <path d="M0 0 H110 Q70 40 0 60 Z" fill="var(--purple)"/>
      <rect x="0" y="150" width="14" height="160" fill="var(--yellow)"/>
      <path d="M210 300 L330 230 V520 Z" fill="var(--pink)"/>
      <path d="M0 560 L90 645 H0 Z" fill="var(--purple)"/>
      <path d="M250 645 Q280 560 330 540 V645 Z" fill="var(--green)"/>
      <line x1="196" y1="78" x2="188" y2="92" stroke="var(--icon-green)" stroke-width="2"/>
    </svg>

    <div class="status-bar"><span>9:41</span><span>●●● ▮</span></div>

    <header class="app-header">
      <svg class="back-arrow" width="20" height="18" viewBox="0 0 20 18" aria-label="Back">
        <path d="M18 9 H3 M9 3 L3 9 L9 15" fill="none" stroke="var(--ink)" stroke-width="2"/>
      </svg>
      <h1 class="screen-title">Badges</h1>
    </header>

    <ul class="badge-list">
      <li class="badge-card">
        <svg class="badge-icon" viewBox="0 0 32 32"><g stroke="var(--icon-purple)" stroke-width="2" fill="none"><path d="M16 3 V29 M4 10 L28 22 M4 22 L28 10"/><circle cx="16" cy="16" r="5"/></g></svg>
        <p class="badge-text">2 point reduction for completing game is under 35 minutes</p>
      </li>
      <li class="badge-card">
        <svg class="badge-icon" viewBox="0 0 32 32"><g stroke="var(--icon-gold)" stroke-width="2" fill="none"><circle cx="16" cy="16" r="12"/><circle cx="16" cy="16" r="7"/></g></svg>
        <p class="badge-text">2 point reduction for sharing the app's selfie pic to social media.</p>
      </li>
      <li class="badge-card">
        <svg class="badge-icon" viewBox="0 0 32 32"><g stroke="var(--icon-green)" stroke-width="2" fill="none"><path d="M11 28 V12 L8 4 M17 12 L20 3 M10 15 H22 V28 H10"/></g></svg>
        <p class="badge-text">4 point reduction for taking Zero clues</p>
      </li>
      <li class="badge-card">
        <svg class="badge-icon" viewBox="0 0 32 32"><g stroke="var(--icon-pink)" stroke-width="2" fill="none"><rect x="4" y="4" width="24" height="24"/><path d="M16 8 L18.5 13.5 L24 14 L20 18 L21 24 L16 21 L11 24 L12 18 L8 14 L13.5 13.5 Z"/></g></svg>
        <p class="badge-text">2 point reduction for taking 1-2 clues entire game</p>
      </li>
      <li class="badge-card">
        <svg class="badge-icon" viewBox="0 0 32 32"><g stroke="var(--icon-purple)" stroke-width="2" fill="none"><circle cx="16" cy="16" r="5"/><path d="M16 3 L19 8 L25 7 L24 13 L29 16 L24 19 L25 25 L19 24 L16 29 L13 24 L7 25 L8 19 L3 16 L8 13 L7 7 L13 8 Z"/></g></svg>
        <p class="badge-text">2 point reduction for having par or less than par score</p>
      </li>
      <li class="badge-card">
        <svg class="badge-icon" viewBox="0 0 32 32"><path d="M16 3 L19.5 12 L29 12.5 L21.5 18.5 L24 28 L16 22.5 L8 28 L10.5 18.5 L3 12.5 L12.5 12 Z" fill="none" stroke="var(--icon-green)" stroke-width="2"/></svg>
        <p class="badge-text">1 point reduction for having multiple hole in ones</p>
      </li>
    </ul>

    <a class="next-button" role="button">NEXT</a>
  </main>
</body>
</html>
```